Party Decoration Set Designs - Rose Gold theme - more example images just added

We are looking for a set of designs for a set of party decorations. It’s a Rose Gold colored theme. I have attached some photos of some glittery rose gold items that I think would go good with the theme. There are also some photos of full sets of decorations in other colors schemes to give an idea of what we are looking for.

We would like to have designs for the items below:

1- Happy Birthday Flag Banner- looking for something unique. Size- 5”X7” WXL

2- hanging swirl cards ( photo examples attached) 4”X6” approx. can be different sizes and shapes.

3- centerpiece designs- photo examples attached. Middle
Piece that’s says Happy Birthday should be 5”X 7” and the smaller surrounding pieces 3X5

4 - round candy stickers and candy wrappers. Examples below. .75 inch

The photos below are of products currently sold. We would like to be very similar to these but just a little different to make our own. And then to have a Happy Birthday banner created to match the theme.

Some of these example photos below are from different themes and colors But I included them because they are the complete set we want to create. First we will do a generic “Happy Birthday” Set with rose gold glitter theme and then later we will add the Sweet 16 birthday theme as well and 40th, 50th etc.

On the centerpieces where the example photos how a large “40”, we would like this to be a larger “Happy Birthday” design. Then surrounded by some smaller designs.
I look forward to receiving your ideas

Target Market(s)

Anyone looking for birthday Peru decorations for a female.

Font styles to use
Other font styles liked:
• Open to designer suggestion

Requirements
Must have
• Happy Birthday Banner, Hanging swirl cards, centerpiece cards, cake topper
Nice to have
• We are certainly open to any creative ideas.
Should not have
• I just now added some example images of a very good set of exactly what we want but its in a different theme. This is a black gold set and our requested design is more feminine and Rose Gold color

```html
<!DOCTYPE html>
<html lang="en">
<head>
<meta charset="utf-8">
<title>Rose Gold Party Badges</title>
<link rel="stylesheet" href="https://fonts.googleapis.com/css2?family=Montserrat:wght@800&family=Parisienne&display=swap">
<style>
  :root {
    --paper: #ffffff;
    --blush: #fbdcd4;
    --blush-light: #fdebe8;
    --rust: #a8443a;
    --maroon: #66201a;
    --gold: #d9a03c;
    --gold-deep: #9c6a1e;
    --dot-tone: #e3aca2;
    --stripe-tone: #f0cfa8;
  }
  html, body {
    margin: 0;
    padding: 0;
    width: 1184px;
    height: 1200px;
    overflow: hidden;
    background: var(--paper);
  }
  .badge-sheet { display: block; width: 1184px; height: 1200px; }
  .glitter { fill: url(#glitterTone); }
  .glitter-stroke { fill: none; stroke: url(#glitterTone); }
  .blush { fill: var(--blush); }
  .blush-light { fill: var(--blush-light); }
  .dot-field { fill: var(--dot-tone); }
  .stripe-field { fill: url(#stripeTone); }
  .maroon-disc { fill: var(--maroon); }
  .maroon-frame { fill: var(--blush-light); stroke: var(--maroon); stroke-width: 20; }
  .cake-slice { fill: var(--rust); }
  .caps {
    font-family: "Montserrat", sans-serif;
    font-weight: 800;
    text-anchor: middle;
  }
  .script {
    font-family: "Parisienne", cursive;
    text-anchor: middle;
  }
  .rust-text { fill: var(--rust); }
  .gold-text { fill: var(--gold); }
  .maroon-text { fill: var(--maroon); }
  .white-text { fill: var(--paper); }
</style>
</head>
<body>
<svg class="badge-sheet" viewBox="0 0 1480 1500" xmlns="http://www.w3.org/2000/svg">
  <defs>
    <linearGradient id="glitterTone" x1="0" y1="0" x2="1" y2="1">
      <stop offset="0" stop-color="#f2c870"/>
      <stop offset="0.5" stop-color="#d39433"/>
      <stop offset="1" stop-color="#a8701f"/>
    </linearGradient>
    <linearGradient id="stripeTone" x1="0" y1="0" x2="1" y2="1">
      <stop offset="0" stop-color="#f6dcc3"/>
      <stop offset="1" stop-color="#ecc79a"/>
    </linearGradient>
  </defs>

  <!-- Star badge -->
  <g class="badge badge-star">
    <polygon class="glitter" role="img" aria-label="Gold glitter star border"
      points="370,42 445,292 715,292 495,455 582,695 370,540 155,695 245,455 22,292 300,292"/>
    <polygon class="blush"
      points="370,165 420,322 592,322 455,420 512,595 370,502 225,595 282,420 148,322 320,322"/>
    <text class="caps rust-text" x="366" y="358" font-size="40">LET’S</text>
    <text class="script rust-text" x="368" y="418" font-size="56">Celebrate</text>
    <rect class="cake-slice" x="336" y="432" width="72" height="58" rx="6"
      role="img" aria-label="Cake slice illustration"/>
  </g>

  <!-- Hexagon badge -->
  <g class="badge badge-hexagon">
    <polygon class="dot-field" role="img" aria-label="Rust polka dot pattern on blush"
      points="930,105 1250,105 1410,385 1250,665 930,665 775,385"/>
    <polygon class="blush-light"
      points="990,198 1195,198 1310,385 1195,575 990,575 875,385"/>
    <polygon class="glitter-stroke" stroke-width="28" role="img" aria-label="Gold glitter hexagon frame"
      points="990,198 1195,198 1310,385 1195,575 990,575 875,385"/>
    <text class="caps rust-text" x="1095" y="325" font-size="56">HAPPY</text>
    <text class="script rust-text" x="1098" y="410" font-size="84">Birthday</text>
    <rect class="cake-slice" x="1042" y="442" width="102" height="96" rx="8"
      role="img" aria-label="Glitter cake slice illustration"/>
  </g>

  <!-- Round badge -->
  <g class="badge badge-round">
    <circle class="glitter" cx="370" cy="1117" r="260" role="img" aria-label="Gold glitter ring"/>
    <circle class="maroon-disc" cx="370" cy="1117" r="210"/>
    <text class="caps gold-text" x="366" y="1030" font-size="62">TIME</text>
    <text class="caps gold-text" x="366" y="1112" font-size="62">TO</text>
    <text class="script white-text" x="376" y="1212" font-size="96">Party</text>
  </g>

  <!-- Diamond badge -->
  <g class="badge badge-diamond">
    <polygon class="stripe-field" role="img" aria-label="Diagonal gold glitter stripes on blush"
      points="1092,780 1415,1100 1092,1420 772,1100"/>
    <polygon class="maroon-frame"
      points="1095,862 1332,1098 1095,1334 856,1098"/>
    <text class="caps gold-text" x="1092" y="1062" font-size="66">LET’S</text>
    <text class="script maroon-text" x="1096" y="1158" font-size="84">Celebrate</text>
  </g>
</svg>
</body>
</html>
```